Website for an electrical contractor :)

We are after a web site which can show pictures of our jobs and our capability in a professional, creative and easily understood way.

----- Brightmoor Electrical ------

We really want a visually good looking website with three sections

Section one:
'Completed projects'
We have a few pictures of jobs which we've completed and would like to show off with a brief description. (see uploads)

Section two:
'Our capabilities'
Just a list of what services we offer

Section three:
We would like a 'contact us' section which people can send us a short msg and upload a file for plans to be able to send to us. We would need their name, phone number and email details. We would also need a short privacy policy saying 'we do not disclose information to third parties'.
We also want to display our contact number and postal address

Good luck :)

Target Market(s)

Adults 25 years+
Business owners
Builders
Real estate agents

Industry/Entity Type

Electrical

Colors

Designer to choose colors to be used in the design.

Requirements
Must have
• Visually appealing
Easy to understand
In the 'Completed projects' section, must have a list for each project we do i can upload pictures for it.

```html
<!DOCTYPE html>
<html lang="en">
<head>
<meta charset="utf-8">
<title>Brightmoor Electrical</title>
<link href="https://fonts.googleapis.com/css2?family=Lato:wght@400;700&family=Oswald:wght@300;400&display=swap" rel="stylesheet">
<style>
:root{
  --red:#e31b23;
  --red-dark:#b8141a;
  --ink:#333;
  --grey:#666;
  --dark:#565656;
  --darker:#4a4a4a;
  --light:#f6f6f6;
  --paper:#fcfcfc;
  --white:#fff;
}
*{margin:0;padding:0;box-sizing:border-box}
html,body{width:1200px;height:2586px;overflow:hidden}
body{position:relative;font-family:'Lato',sans-serif;color:var(--ink);background:var(--paper)}
.abs{position:absolute}

/* header */
.header{left:0;top:0;width:1200px;height:119px;background:var(--white)}
.brand{left:124px;top:36px;display:flex;align-items:center;gap:14px}
.brand-dot{width:30px;height:30px;border-radius:50%;background:var(--red)}
.brand-name{font-size:40px;font-weight:400;color:#666;letter-spacing:-0.5px}
.contact-top{left:858px;top:12px;font-size:12px;line-height:19px;color:var(--ink)}
.contact-top li{list-style:none;display:flex;align-items:flex-start;gap:10px}
.contact-top svg{flex:none;margin-top:4px}

/* nav */
.nav{left:0;top:119px;width:1200px;height:38px;background:var(--red)}
.nav a{position:absolute;top:0;height:38px;line-height:38px;color:var(--white);font-size:12px;text-decoration:none;text-transform:uppercase;transform:translateX(-50%);white-space:nowrap;padding:0 17px}
.nav a.active{background:var(--red-dark)}

/* hero */
.hero{left:0;top:157px;width:1200px;height:495px;background:linear-gradient(180deg,#6d9ed8 0%,#c7d9ef 30%,#8b9098 45%,#5d6168 70%,#b4b6b8 88%,#d2d2d0 100%)}
.hero-arrow{width:38px;height:38px;border-radius:50%;display:flex;align-items:center;justify-content:center}
.hero-arrow.prev{left:24px;top:357px;background:var(--white)}
.hero-arrow.next{left:1146px;top:357px;background:var(--red)}

/* section titles */
.section-title{left:0;width:1200px;text-align:center;font-family:'Oswald',sans-serif;font-weight:300;font-size:36px;color:var(--red);text-transform:uppercase;letter-spacing:0.5px}
.title-rule{left:50%;transform:translateX(-50%)}

/* about */
.about{left:0;top:652px;width:1200px;height:400px;background:var(--paper)}
.about-photo{left:124px;top:762px;width:462px;height:243px;border:2px solid #555;background:linear-gradient(180deg,#5e93d3 0%,#9cc0e6 35%,#c9c3b6 55%,#8e8a82 78%,#b9b4aa 100%)}
.about-text{left:612px;top:755px;width:464px;font-size:11.5px;line-height:16.6px;color:var(--ink)}
.about-text p{margin-bottom:17px}
.btn-more{left:612px;top:969px;width:138px;height:38px;background:var(--dark);color:var(--white);font-size:11.5px;font-weight:700;border-radius:3px;display:flex;align-items:center;justify-content:center;gap:8px;text-transform:uppercase}

/* projects */
.projects{left:0;top:1052px;width:1200px;height:491px;background:var(--light)}
.project{width:219px;height:143px;border:1px solid #888;border-radius:4px}
.project-tools{display:flex;gap:8px;position:absolute;left:70px;top:54px}
.project-tools span{width:34px;height:34px;background:var(--red);display:flex;align-items:center;justify-content:center;border-radius:2px}
.pager{left:576px;top:1497px;display:flex;gap:7px}
.pager i{width:12px;height:12px;border-radius:50%;background:var(--red);border:2px solid var(--red)}
.pager i.on{background:transparent}

/* services */
.services{left:0;top:1543px;width:1200px;height:417px;background:var(--paper)}
.services-head{font-family:'Oswald',sans-serif;font-weight:300;font-size:22px;color:#444;text-transform:uppercase}
.service-list{list-style:none;font-size:12px;line-height:19.7px;color:var(--ink);width:215px}
.service-list li{display:flex;gap:9px;align-items:flex-start}
.service-list svg{flex:none;margin-top:5px}

/* contact */
.contact{left:0;top:1960px;width:1200px;height:626px;background:var(--dark)}
.contact .section-title{color:var(--white)}
.field{left:124px;width:381px;height:45px;background:var(--white);font-size:10px;color:#444;padding:14px 13px}
.field.msg{height:140px}
.btn-send{left:124px;top:2405px;width:112px;height:43px;background:var(--red);color:var(--white);font-size:14px;font-weight:700;display:flex;align-items:center;justify-content:center}
.btn-clear{left:245px;top:2405px;width:110px;height:43px;border:2px solid var(--white);color:var(--white);font-size:14px;font-weight:700;display:flex;align-items:center;justify-content:center}
.map{left:531px;top:2067px;width:545px;height:381px;background:linear-gradient(135deg,#ecebe6 0%,#e3e1da 50%,#d8d6ce 100%)}
.map-bar{left:531px;top:2353px;width:545px;height:95px;background:rgba(90,90,90,0.85);color:var(--white);font-size:13.5px;line-height:21px}
.map-bar .item{position:absolute;display:flex;gap:10px;align-items:flex-start}
.map-bar svg{flex:none;margin-top:3px}
.footer-rule{left:124px;top:2508px;width:952px;height:1px;background:#6c6c6c}
.footer-text{left:124px;top:2539px;font-size:10px;color:#bdbdbd}
.footer-text span{margin:0 9px}
.social{left:968px;top:2541px;display:flex;gap:14px}
.social i{width:9px;height:9px;border-radius:50%;background:#9a9a9a}
</style>
</head>
<body>

<header class="header abs">
  <div class="brand abs"><span class="brand-dot"></span><span class="brand-name">Brightmoor Electrical</span></div>
  <ul class="contact-top abs">
    <li><svg width="10" height="10" viewBox="0 0 10 10"><path d="M2 0.5 L3.8 2.6 L2.8 3.8 Q4 6.2 6.2 7.2 L7.4 6.2 L9.5 8 L8.3 9.5 Q1.5 8.5 0.5 1.7Z" fill="#e31b23"/></svg>0412 555 018</li>
    <li><svg width="10" height="10" viewBox="0 0 10 10"><path d="M2 0.5 L3.8 2.6 L2.8 3.8 Q4 6.2 6.2 7.2 L7.4 6.2 L9.5 8 L8.3 9.5 Q1.5 8.5 0.5 1.7Z" fill="#e31b23"/></svg>08 9555 0142</li>
    <li><svg width="11" height="9" viewBox="0 0 11 9"><rect x="0.6" y="0.6" width="9.8" height="7.8" fill="none" stroke="#e31b23" stroke-width="1.2"/><path d="M0.6 0.6 L5.5 5 L10.4 0.6" fill="none" stroke="#e31b23" stroke-width="1.2"/></svg>info@brightmoorelectrical.com.au</li>
    <li><svg width="10" height="13" viewBox="0 0 10 13"><path d="M5 0 A5 5 0 0 1 10 5 C10 8 5 13 5 13 C5 13 0 8 0 5 A5 5 0 0 1 5 0Z" fill="#e31b23"/><circle cx="5" cy="5" r="1.8" fill="#fff"/></svg><span>P.O Box 418 Harbourview W.A 6099<br>A.B.N: 12 345 678 901</span></li>
  </ul>
</header>

<nav class="nav abs">
  <a class="active" style="left:236px">Home</a>
  <a style="left:345px">About Us</a>
  <a style="left:467px">Services</a>
  <a style="left:626px">Completed Projects</a>
  <a style="left:809px">Our Capabilities</a>
  <a style="left:955px">Contact</a>
</nav>

<div class="hero abs" role="img" aria-label="Photograph of a modern two-storey industrial warehouse building under a cloudy blue sky"></div>
<div class="hero-arrow prev abs"><svg width="10" height="12" viewBox="0 0 10 12"><path d="M7 1 L2 6 L7 11" fill="none" stroke="#333" stroke-width="2.4"/></svg></div>
<div class="hero-arrow next abs"><svg width="10" height="12" viewBox="0 0 10 12"><path d="M3 1 L8 6 L3 11" fill="none" stroke="#fff" stroke-width="2.4"/></svg></div>

<section class="about abs"></section>
<h2 class="section-title abs" style="top:680px">About Us</h2>
<svg class="title-rule abs" style="top:726px" width="150" height="10" viewBox="0 0 150 10"><line x1="6" y1="5" x2="144" y2="5" stroke="#e31b23" stroke-width="1.2"/><circle cx="4" cy="5" r="3" fill="none" stroke="#e31b23" stroke-width="1.2"/><circle cx="146" cy="5" r="3" fill="none" stroke="#e31b23" stroke-width="1.2"/></svg>
<div class="about-photo abs" role="img" aria-label="Photograph of a finished single-storey home with paved driveway"></div>
<div class="about-text abs">
  <p>Lorem ipsum dolor sit amet conse ctetur adipisicing elit, sed do eiusmod tempor incididunt ut labore et dolore magna aliqua. Ut enim ad minim veniam, quis nostrud exercitation ullamco laboris nisi ut aliquip ex ea commodo consequat.</p>
  <p>Lorem ipsum dolor sit amet conse ctetur adipisicing elit, sed do eiusmod tempor incididunt ut labore et dolore magna aliqua. Ut enim ad minim veniam, quis nostrud exercitation ullamco laboris nisi ut aliquip ex ea commodo consequat.</p>
  <p>Lorem ipsum dolor sit amet conse ctetur adipisicing elit, sed do eiusmod tempor incididunt ut labore et dolore magna aliqua. Ut enim ad minim veniam, quis nostrud exercitation ullamco laboris nisi ut aliquip ex ea commodo consequat.</p>
</div>
<div class="btn-more abs">Learn More <svg width="11" height="11" viewBox="0 0 11 11"><circle cx="5.5" cy="5.5" r="5.5" fill="#fff"/><path d="M4.3 3 L6.8 5.5 L4.3 8" fill="none" stroke="#565656" stroke-width="1.6"/></svg></div>

<section class="projects abs"></section>
<h2 class="section-title abs" style="top:1075px">Our Projects</h2>
<svg class="title-rule abs" style="top:1122px" width="210" height="10" viewBox="0 0 210 10"><line x1="6" y1="5" x2="204" y2="5" stroke="#e31b23" stroke-width="1.2"/><circle cx="4" cy="5" r="3" fill="none" stroke="#e31b23" stroke-width="1.2"/><circle cx="206" cy="5" r="3" fill="none" stroke="#e31b23" stroke-width="1.2"/></svg>

<div class="project abs" style="left:124px;top:1158px;background:linear-gradient(160deg,#b9bcc2,#8f9398)" role="img" aria-label="Project photo: signage on a glass office front">
  <div class="project-tools">
    <span><svg width="16" height="16" viewBox="0 0 16 16"><path d="M6.5 9.5 L9.5 6.5 M7 4.5 L8.8 2.7 A2.6 2.6 0 0 1 13.3 7.2 L11.5 9 M9 11.5 L7.2 13.3 A2.6 2.6 0 0 1 2.7 8.8 L4.5 7" fill="none" stroke="#fff" stroke-width="1.8"/></svg></span>
    <span><svg width="16" height="16" viewBox="0 0 16 16"><circle cx="6.5" cy="6.5" r="4.5" fill="none" stroke="#fff" stroke-width="2"/><line x1="10" y1="10" x2="14.5" y2="14.5" stroke="#fff" stroke-width="2.2"/></svg></span>
  </div>
</div>
<div class="project abs" style="left:369px;top:1158px;background:linear-gradient(180deg,#cbb89a,#8c7258)" role="img" aria-label="Project photo: kitchen fit-out with downlights"></div>
<div class="project abs" style="left:612px;top:1158px;background:linear-gradient(180deg,#e8e4dc,#a9a196)" role="img" aria-label="Project photo: reception lounge with ceiling lighting"></div>
<div class="project abs" style="left:857px;top:1158px;background:linear-gradient(180deg,#d9d4cc,#6d6661)" role="img" aria-label="Project photo: open function room with carpet"></div>
<div class="project abs" style="left:124px;top:1327px;background:linear-gradient(180deg,#8a8782,#4d4a45)" role="img" aria-label="Project photo: empty warehouse interior"></div>
<div class="project abs" style="left:369px;top:1327px;background:linear-gradient(180deg,#6fa0dc,#c9c8c4 55%,#a39c90)" role="img" aria-label="Project photo: commercial building under construction"></div>
<div class="project abs" style="left:612px;top:1327px;background:linear-gradient(180deg,#8e8678,#5a5147)" role="img" aria-label="Project photo: slab reinforcement with conduit"></div>
<div class="project abs" style="left:857px;top:1327px;background:linear-gradient(180deg,#3f7ed4,#dedcd7 60%,#b3aea5)" role="img" aria-label="Project photo: white concrete warehouse exterior"></div>
<div class="pager abs"><i class="on"></i><i></i><i></i></div>

<section class="services abs"></section>
<h2 class="section-title abs" style="top:1575px">Our Services</h2>
<svg class="title-rule abs" style="top:1622px" width="180" height="10" viewBox="0 0 180 10"><line x1="6" y1="5" x2="174" y2="5" stroke="#e31b23" stroke-width="1.2"/><circle cx="4" cy="5" r="3" fill="none" stroke="#e31b23" stroke-width="1.2"/><circle cx="176" cy="5" r="3" fill="none" stroke="#e31b23" stroke-width="1.2"/></svg>

<div class="services-head abs" style="left:124px;top:1655px">Residential</div>
<svg class="abs" style="left:230px;top:1665px" width="357" height="8" viewBox="0 0 357 8"><circle cx="4" cy="4" r="3" fill="none" stroke="#666" stroke-width="1.2"/><line x1="7" y1="4" x2="357" y2="4" stroke="#999" stroke-width="1"/></svg>
<div class="services-head abs" style="left:612px;top:1655px">Commercial / Industrial</div>
<svg class="abs" style="left:818px;top:1665px" width="258" height="8" viewBox="0 0 258 8"><circle cx="4" cy="4" r="3" fill="none" stroke="#666" stroke-width="1.2"/><line x1="7" y1="4" x2="258" y2="4" stroke="#999" stroke-width="1"/></svg>

<ul class="service-list abs" style="left:124px;top:1702px">
  <li><svg width="10" height="10" viewBox="0 0 10 10"><circle cx="5" cy="5" r="5" fill="#e31b23"/><path d="M4 2.8 L6.2 5 L4 7.2" fill="none" stroke="#fff" stroke-width="1.5"/></svg>24hr Support / faults</li>
  <li><svg width="10" height="10" viewBox="0 0 10 10"><circle cx="5" cy="5" r="5" fill="#e31b23"/><path d="M4 2.8 L6.2 5 L4 7.2" fill="none" stroke="#fff" stroke-width="1.5"/></svg>RCD (Safety Switch) installations</li>
  <li><svg width="10" height="10" viewBox="0 0 10 10"><circle cx="5" cy="5" r="5" fill="#e31b23"/><path d="M4 2.8 L6.2 5 L4 7.2" fill="none" stroke="#fff" stroke-width="1.5"/></svg>Smoke alarms</li>
  <li><svg width="10" height="10" viewBox="0 0 10 10"><circle cx="5" cy="5" r="5" fill="#e31b23"/><path d="M4 2.8 L6.2 5 L4 7.2" fill="none" stroke="#fff" stroke-width="1.5"/></svg>Power points</li>
  <li><svg width="10" height="10" viewBox="0 0 10 10"><circle cx="5" cy="5" r="5" fill="#e31b23"/><path d="M4 2.8 L6.2 5 L4 7.2" fill="none" stroke="#fff" stroke-width="1.5"/></svg>Lighting points</li>
  <li><svg width="10" height="10" viewBox="0 0 10 10"><circle cx="5" cy="5" r="5" fill="#e31b23"/><path d="M4 2.8 L6.2 5 L4 7.2" fill="none" stroke="#fff" stroke-width="1.5"/></svg>External lighting</li>
  <li><svg width="10" height="10" viewBox="0 0 10 10"><circle cx="5" cy="5" r="5" fill="#e31b23"/><path d="M4 2.8 L6.2 5 L4 7.2" fill="none" stroke="#fff" stroke-width="1.5"/></svg>Sensor lighting</li>
  <li><svg width="10" height="10" viewBox="0 0 10 10"><circle cx="5" cy="5" r="5" fill="#e31b23"/><path d="M4 2.8 L6.2 5 L4 7.2" fill="none" stroke="#fff" stroke-width="1.5"/></svg>Switching</li>
  <li><svg width="10" height="10" viewBox="0 0 10 10"><circle cx="5" cy="5" r="5" fill="#e31b23"/><path d="M4 2.8 L6.2 5 L4 7.2" fill="none" stroke="#fff" stroke-width="1.5"/></svg>Antennas and Arial points</li>
  <li><svg width="10" height="10" viewBox="0 0 10 10"><circle cx="5" cy="5" r="5" fill="#e31b23"/><path d="M4 2.8 L6.2 5 L4 7.2" fill="none" stroke="#fff" stroke-width="1.5"/></svg>Dimmers</li>
  <li><svg width="10" height="10" viewBox="0 0 10 10"><circle cx="5" cy="5" r="5" fill="#e31b23"/><path d="M4 2.8 L6.2 5 L4 7.2" fill="none" stroke="#fff" stroke-width="1.5"/></svg>Ceiling fans</li>
</ul>
<ul class="service-list abs" style="left:369px;top:1702px">
  <li><svg width="10" height="10" viewBox="0 0 10 10"><circle cx="5" cy="5" r="5" fill="#e31b23"/><path d="M4 2.8 L6.2 5 L4 7.2" fill="none" stroke="#fff" stroke-width="1.5"/></svg>Exhaust fans</li>
  <li><svg width="10" height="10" viewBox="0 0 10 10"><circle cx="5" cy="5" r="5" fill="#e31b23"/><path d="M4 2.8 L6.2 5 L4 7.2" fill="none" stroke="#fff" stroke-width="1.5"/></svg>Kitchen / Bathroom Projects</li>
  <li><svg width="10" height="10" viewBox="0 0 10 10"><circle cx="5" cy="5" r="5" fill="#e31b23"/><path d="M4 2.8 L6.2 5 L4 7.2" fill="none" stroke="#fff" stroke-width="1.5"/></svg>Re-wires</li>
  <li><svg width="10" height="10" viewBox="0 0 10 10"><circle cx="5" cy="5" r="5" fill="#e31b23"/><path d="M4 2.8 L6.2 5 L4 7.2" fill="none" stroke="#fff" stroke-width="1.5"/></svg>Smart wiring</li>
  <li><svg width="10" height="10" viewBox="0 0 10 10"><circle cx="5" cy="5" r="5" fill="#e31b23"/><path d="M4 2.8 L6.2 5 L4 7.2" fill="none" stroke="#fff" stroke-width="1.5"/></svg>Phone points</li>
  <li><svg width="10" height="10" viewBox="0 0 10 10"><circle cx="5" cy="5" r="5" fill="#e31b23"/><path d="M4 2.8 L6.2 5 L4 7.2" fill="none" stroke="#fff" stroke-width="1.5"/></svg>Data points</li>
  <li><svg width="10" height="10" viewBox="0 0 10 10"><circle cx="5" cy="5" r="5" fill="#e31b23"/><path d="M4 2.8 L6.2 5 L4 7.2" fill="none" stroke="#fff" stroke-width="1.5"/></svg>Mains/sub mains cabling</li>
  <li><svg width="10" height="10" viewBox="0 0 10 10"><circle cx="5" cy="5" r="5" fill="#e31b23"/><path d="M4 2.8 L6.2 5 L4 7.2" fill="none" stroke="#fff" stroke-width="1.5"/></svg>Switchboard installations</li>
  <li><svg width="10" height="10" viewBox="0 0 10 10"><circle cx="5" cy="5" r="5" fill="#e31b23"/><path d="M4 2.8 L6.2 5 L4 7.2" fill="none" stroke="#fff" stroke-width="1.5"/></svg>Compliance investigations</li>
  <li><svg width="10" height="10" viewBox="0 0 10 10"><circle cx="5" cy="5" r="5" fill="#e31b23"/><path d="M4 2.8 L6.2 5 L4 7.2" fill="none" stroke="#fff" stroke-width="1.5"/></svg>Concrete and wall chasing</li>
  <li><svg width="10" height="10" viewBox="0 0 10 10"><circle cx="5" cy="5" r="5" fill="#e31b23"/><path d="M4 2.8 L6.2 5 L4 7.2" fill="none" stroke="#fff" stroke-width="1.5"/></svg>Temporary builders site power</li>
</ul>
<ul class="service-list abs" style="left:612px;top:1702px">
  <li><svg width="10" height="10" viewBox="0 0 10 10"><circle cx="5" cy="5" r="5" fill="#e31b23"/><path d="M4 2.8 L6.2 5 L4 7.2" fill="none" stroke="#fff" stroke-width="1.5"/></svg>24hr Support / faults</li>
  <li><svg width="10" height="10" viewBox="0 0 10 10"><circle cx="5" cy="5" r="5" fill="#e31b23"/><path d="M4 2.8 L6.2 5 L4 7.2" fill="none" stroke="#fff" stroke-width="1.5"/></svg>Lighting/power design</li>
  <li><svg width="10" height="10" viewBox="0 0 10 10"><circle cx="5" cy="5" r="5" fill="#e31b23"/><path d="M4 2.8 L6.2 5 L4 7.2" fill="none" stroke="#fff" stroke-width="1.5"/></svg>Commercial lighting</li>
  <li><svg width="10" height="10" viewBox="0 0 10 10"><circle cx="5" cy="5" r="5" fill="#e31b23"/><path d="M4 2.8 L6.2 5 L4 7.2" fill="none" stroke="#fff" stroke-width="1.5"/></svg>Emergency and exit lighting</li>
  <li><svg width="10" height="10" viewBox="0 0 10 10"><circle cx="5" cy="5" r="5" fill="#e31b23"/><path d="M4 2.8 L6.2 5 L4 7.2" fill="none" stroke="#fff" stroke-width="1.5"/></svg>Led strip lighting</li>
  <li><svg width="10" height="10" viewBox="0 0 10 10"><circle cx="5" cy="5" r="5" fill="#e31b23"/><path d="M4 2.8 L6.2 5 L4 7.2" fill="none" stroke="#fff" stroke-width="1.5"/></svg>Energy efficient lighting</li>
  <li><svg width="10" height="10" viewBox="0 0 10 10"><circle cx="5" cy="5" r="5" fill="#e31b23"/><path d="M4 2.8 L6.2 5 L4 7.2" fill="none" stroke="#fff" stroke-width="1.5"/></svg>Temporary lighting</li>
  <li><svg width="10" height="10" viewBox="0 0 10 10"><circle cx="5" cy="5" r="5" fill="#e31b23"/><path d="M4 2.8 L6.2 5 L4 7.2" fill="none" stroke="#fff" stroke-width="1.5"/></svg>Illuminated signage</li>
  <li><svg width="10" height="10" viewBox="0 0 10 10"><circle cx="5" cy="5" r="5" fill="#e31b23"/><path d="M4 2.8 L6.2 5 L4 7.2" fill="none" stroke="#fff" stroke-width="1.5"/></svg>Switchboard relocations</li>
  <li><svg width="10" height="10" viewBox="0 0 10 10"><circle cx="5" cy="5" r="5" fill="#e31b23"/><path d="M4 2.8 L6.2 5 L4 7.2" fill="none" stroke="#fff" stroke-width="1.5"/></svg>Maintenance</li>
</ul>
<ul class="service-list abs" style="left:857px;top:1702px">
  <li><svg width="10" height="10" viewBox="0 0 10 10"><circle cx="5" cy="5" r="5" fill="#e31b23"/><path d="M4 2.8 L6.2 5 L4 7.2" fill="none" stroke="#fff" stroke-width="1.5"/></svg>RCD installation</li>
  <li><svg width="10" height="10" viewBox="0 0 10 10"><circle cx="5" cy="5" r="5" fill="#e31b23"/><path d="M4 2.8 L6.2 5 L4 7.2" fill="none" stroke="#fff" stroke-width="1.5"/></svg>Phone/data points</li>
  <li><svg width="10" height="10" viewBox="0 0 10 10"><circle cx="5" cy="5" r="5" fill="#e31b23"/><path d="M4 2.8 L6.2 5 L4 7.2" fill="none" stroke="#fff" stroke-width="1.5"/></svg>Data cabinets</li>
  <li><svg width="10" height="10" viewBox="0 0 10 10"><circle cx="5" cy="5" r="5" fill="#e31b23"/><path d="M4 2.8 L6.2 5 L4 7.2" fill="none" stroke="#fff" stroke-width="1.5"/></svg>Data Networking</li>
  <li><svg width="10" height="10" viewBox="0 0 10 10"><circle cx="5" cy="5" r="5" fill="#e31b23"/><path d="M4 2.8 L6.2 5 L4 7.2" fill="none" stroke="#fff" stroke-width="1.5"/></svg>IDF installations/relocations</li>
  <li><svg width="10" height="10" viewBox="0 0 10 10"><circle cx="5" cy="5" r="5" fill="#e31b23"/><path d="M4 2.8 L6.2 5 L4 7.2" fill="none" stroke="#fff" stroke-width="1.5"/></svg>All power requirements</li>
  <li><svg width="10" height="10" viewBox="0 0 10 10"><circle cx="5" cy="5" r="5" fill="#e31b23"/><path d="M4 2.8 L6.2 5 L4 7.2" fill="none" stroke="#fff" stroke-width="1.5"/></svg><span>All three phase power require<br>ments</span></li>
  <li><svg width="10" height="10" viewBox="0 0 10 10"><circle cx="5" cy="5" r="5" fill="#e31b23"/><path d="M4 2.8 L6.2 5 L4 7.2" fill="none" stroke="#fff" stroke-width="1.5"/></svg>Electrical rip outs / Disconnections</li>
  <li><svg width="10" height="10" viewBox="0 0 10 10"><circle cx="5" cy="5" r="5" fill="#e31b23"/><path d="M4 2.8 L6.2 5 L4 7.2" fill="none" stroke="#fff" stroke-width="1.5"/></svg>Thermal imaging scans</li>
  <li><svg width="10" height="10" viewBox="0 0 10 10"><circle cx="5" cy="5" r="5" fill="#e31b23"/><path d="M4 2.8 L6.2 5 L4 7.2" fill="none" stroke="#fff" stroke-width="1.5"/></svg>Concrete and wall chasing</li>
</ul>

<section class="contact abs"></section>
<h2 class="section-title abs" style="top:1980px">Contact Us</h2>
<svg class="title-rule abs" style="top:2027px" width="166" height="10" viewBox="0 0 166 10"><line x1="6" y1="5" x2="160" y2="5" stroke="#fff" stroke-width="1.2"/><circle cx="4" cy="5" r="3" fill="none" stroke="#fff" stroke-width="1.2"/><circle cx="162" cy="5" r="3" fill="none" stroke="#fff" stroke-width="1.2"/></svg>

<div class="field abs" style="top:2067px">Name :</div>
<div class="field abs" style="top:2127px">Phone :</div>
<div class="field abs" style="top:2188px">Email Address :</div>
<div class="field msg abs" style="top:2250px">Message :</div>
<div class="btn-send abs">SEND</div>
<div class="btn-clear abs">CLEAR</div>

<div class="map abs" role="img" aria-label="Street map showing the office location with a red marker"></div>
<div class="map-bar abs">
  <div class="item" style="left:12px;top:25px"><svg width="11" height="14" viewBox="0 0 10 13"><path d="M5 0 A5 5 0 0 1 10 5 C10 8 5 13 5 13 C5 13 0 8 0 5 A5 5 0 0 1 5 0Z" fill="#fff"/><circle cx="5" cy="5" r="1.8" fill="#5a5a5a"/></svg><span>P.O Box 418 Harbourview W.A 6099<br>A.B.N: 12 345 678 901</span></div>
  <div class="item" style="left:328px;top:22px"><svg width="12" height="12" viewBox="0 0 10 10"><path d="M2 0.5 L3.8 2.6 L2.8 3.8 Q4 6.2 6.2 7.2 L7.4 6.2 L9.5 8 L8.3 9.5 Q1.5 8.5 0.5 1.7Z" fill="#fff"/></svg>0412 555 018</div>
  <div class="item" style="left:328px;top:56px"><svg width="12" height="12" viewBox="0 0 10 10"><path d="M2 0.5 L3.8 2.6 L2.8 3.8 Q4 6.2 6.2 7.2 L7.4 6.2 L9.5 8 L8.3 9.5 Q1.5 8.5 0.5 1.7Z" fill="#fff"/></svg>08 9555 0142</div>
</div>

<div class="footer-rule abs"></div>
<div class="footer-text abs">© Copy Right 2013-2015 Brightmoor Electrical .<span>|</span>Privacy Policy<span>|</span>All rights reserved.</div>
<div class="social abs" aria-label="Social links"><i></i><i></i><i></i><i></i><i></i></div>

</body>
</html>
```